Need a new logo/business card for a cafe

I need a new logo and business card for a café. The café is called "Ladle", and we have a reputation for making a high quality cup of espresso coffee. I would like the business card design to reflect this "high quality". Our baristas craft our customers coffee with care to achieve this result. I would like to see designs that include a warm latte brown color. The card will be single sided to allow the rear to be used as a loyalty card which means the design will need to include space for our business address, phone number, and facebook page details. The uploaded logo is already in use on the café front window, and if it can be incorporated or used that would be great, but I am open to completely new designs as well. Thank you.
Updates
Thank you to all for the submissions. There's quite a few I like now, the hardest part will be choosing! I've set up a poll for added feedback from my own contacts and will wait on results from that.
Hello, more great designs coming in, thank you very much. There's quite a few that I really like, so my biggest challenge is going to be choosing one. Thanks again for your time, and I'll get onto the hard task of making that choice. Marisa
Industry/Entity Type
Cafe
Look and feel
Each slider illustrates characteristics of the customer's brand and the style your logo design should communicate.

```html
<!DOCTYPE html>
<html lang="en">
<head>
<meta charset="UTF-8">
<title>Ladle – Business Card</title>
<link rel="stylesheet" href="https://fonts.googleapis.com/css2?family=Gabriela&display=swap">
<style>
  :root {
    --page-bg: #efefef;
    --card-bg: #f0f0f0;
    --frame-brown: #532913;
    --latte-brown: #5a2a12;
    --label-ink: #111111;
  }
  html, body {
    margin: 0;
    padding: 0;
    width: 1200px;
    height: 720px;
    overflow: hidden;
    background: var(--page-bg);
  }
  .canvas {
    position: relative;
    width: 1200px;
    height: 720px;
    background: var(--page-bg);
    font-family: "Gabriela", Georgia, serif;
  }
  .card-frame {
    position: absolute;
    left: 39px;
    top: 39px;
    width: 1125px;
    height: 641px;
    background: var(--frame-brown);
  }
  .card-face {
    position: absolute;
    left: 42px;
    top: 39px;
    width: 1039px;
    height: 562px;
    background: var(--card-bg);
  }
  .brand-name {
    position: absolute;
    left: 66px;
    top: 70px;
    margin: 0;
    font-size: 150px;
    font-weight: 400;
    line-height: 1;
    color: var(--latte-brown);
  }
  .contact-list {
    position: absolute;
    left: 102px;
    top: 294px;
    margin: 0;
    padding: 0;
    list-style: none;
  }
  .contact-item {
    display: flex;
    align-items: center;
    height: 80px;
    font-size: 33px;
  }
  .cup-icon {
    width: 44px;
    height: 56px;
    margin-right: 20px;
    flex: none;
  }
  .contact-label {
    width: 258px;
    color: var(--label-ink);
    white-space: nowrap;
  }
  .contact-value {
    color: var(--latte-brown);
    white-space: nowrap;
  }
</style>
</head>
<body>
<main class="canvas">
  <section class="card-frame">
    <div class="card-face">
      <h1 class="brand-name">Ladle</h1>

      <svg width="0" height="0" style="position:absolute">
        <defs>
          <symbol id="coffee-cup" viewBox="0 0 44 56">
            <path d="M22 4 q-5 5 0 9 q5 4 0 9" fill="none" stroke="var(--latte-brown)" stroke-width="2" stroke-linecap="round"/>
            <path d="M10 28 h24 v6 q0 10 -12 10 q-12 0 -12 -10 z" fill="var(--latte-brown)"/>
            <path d="M34 31 q7 0 6 5 q-1 5 -7 4" fill="none" stroke="var(--latte-brown)" stroke-width="2.5"/>
            <ellipse cx="22" cy="48" rx="18" ry="4" fill="none" stroke="var(--latte-brown)" stroke-width="2.5"/>
          </symbol>
        </defs>
      </svg>

      <ul class="contact-list">
        <li class="contact-item">
          <svg class="cup-icon" aria-hidden="true"><use href="#coffee-cup"/></svg>
          <span class="contact-label">Address</span>
          <span class="contact-value">: Your Company Address</span>
        </li>
        <li class="contact-item">
          <svg class="cup-icon" aria-hidden="true"><use href="#coffee-cup"/></svg>
          <span class="contact-label">Contact Number</span>
          <span class="contact-value">: Your Contact Details</span>
        </li>
        <li class="contact-item">
          <svg class="cup-icon" aria-hidden="true"><use href="#coffee-cup"/></svg>
          <span class="contact-label">Page Details</span>
          <span class="contact-value">: Your Page Details</span>
        </li>
      </ul>
    </div>
  </section>
</main>
</body>
</html>
```